Oversized Post card design

Need a post card design for rebrand, old post card attached for reference but some new content logos and colors. Id like to see new designs please use the one i posted as a reference of the type of design we like

Requirements
Must have
• Pricing page should no longer have "metered" plans only unlimited with these:
• 1 User: $29.99
• 2-10: $24.99/user
• 11-49: $21.99/user
• 50+: Contact Us!
• Add Ons:
• Call Recording: Starting at $5/user
• Additional Local Numbers: $1.99/number
• Fax to email: Starting at $8/user
• Toll Free Numbers: 1.99/number plus usage

```html
<!DOCTYPE html>
<html lang="en">
<head>
<meta charset="utf-8">
<title>Pricing Postcard</title>
<link rel="stylesheet" href="https://fonts.googleapis.com/css2?family=Lato:wght@300;400;700;900&display=swap">
<style>
:root{
  --sky-top:#c9d6e2;
  --sky-bottom:#eef2f6;
  --purple:#7b2f93;
  --cyan:#29b5e0;
  --cyan-light:#3fc3ea;
  --teal:#1c8fb8;
  --teal-dark:#0f5d7c;
  --price:#6a2c8e;
  --ink:#2c2c2c;
  --cell:#f2f3f6;
  --white:#ffffff;
  --footer:#111111;
}
*{margin:0;padding:0;box-sizing:border-box}
html,body{width:1200px;height:776px;overflow:hidden}
body{font-family:"Lato",sans-serif;background:var(--white)}
.card{position:relative;width:1200px;height:776px;overflow:hidden;
  background:linear-gradient(180deg,var(--sky-top) 0%,var(--sky-bottom) 60%,#dfe6ee 100%)}
.backdrop{position:absolute;inset:0}
.brand{position:absolute;left:58px;top:62px;display:flex;align-items:center;gap:16px}
.brand-mark{width:48px;height:48px;background:var(--purple)}
.brand-name{font-weight:700;font-size:46px;letter-spacing:3px;color:#4a4a4a}
.page-title{position:absolute;left:840px;top:58px;font-weight:400;font-size:58px;color:var(--white);letter-spacing:1px}
.plan-panel{position:absolute;left:65px;top:172px;width:1065px;height:323px;
  background:linear-gradient(135deg,var(--teal) 0%,#2aa6d0 60%,#1b7ea6 100%)}
.plan-title{position:absolute;left:183px;top:192px;font-weight:400;font-size:39px;color:var(--white)}
.plan-table{position:absolute;left:134px;top:240px;width:406px;height:202px;background:var(--teal-dark);border-radius:4px}
.plan-row{position:absolute;left:150px;height:40px;display:flex;gap:8px}
.plan-users,.plan-price{background:var(--white);display:flex;align-items:center}
.plan-users{width:168px;padding-left:9px;font-size:23px;color:var(--ink)}
.plan-price{width:200px;padding-left:10px;font-size:21px;color:var(--ink)}
.plan-price b{color:var(--price);font-weight:900;font-size:25px}
.plan-price sup{color:var(--price);font-weight:900;font-size:14px;margin-right:8px}
.plan-price .contact{font-size:24px}
.devices{position:absolute;left:585px;top:225px;width:475px;height:235px;
  background:radial-gradient(ellipse at center,#e8eef4 0%,#a9c7d8 55%,rgba(40,150,200,0) 80%)}
.addons-tab{position:absolute;left:67px;top:452px;width:236px;height:48px;background:var(--cyan-light);
  border-radius:4px 4px 0 0;font-size:31px;color:var(--white);padding:8px 0 0 19px}
.addons-panel{position:absolute;left:67px;top:493px;width:1063px;height:187px;background:var(--cyan-light);border-radius:0 4px 4px 4px}
.addon{position:absolute;height:50px;display:flex;gap:7px}
.addon-icon{width:46px;height:50px;background:var(--cell);display:flex;align-items:center;justify-content:center}
.addon-icon svg{width:26px;height:26px;fill:var(--price)}
.addon-name{width:236px;background:var(--cell);font-size:21px;color:var(--ink);display:flex;align-items:center;padding-left:12px}
.addon-price{width:186px;background:var(--cell);font-size:17px;font-weight:900;color:var(--price);display:flex;flex-direction:column;justify-content:center;padding-left:9px;line-height:1.15}
.addon-price small{font-size:13px;font-weight:700}
.footer{position:absolute;left:0;top:703px;width:1200px;height:49px;background:var(--footer);
  display:flex;align-items:center;justify-content:center;gap:30px;font-weight:700;font-size:24px;color:var(--cyan)}
</style>
</head>
<body>
<div class="card">
  <svg class="backdrop" width="1200" height="776" viewBox="0 0 1200 776" aria-hidden="true">
    <defs>
      <linearGradient id="violet" x1="0" y1="0" x2="1" y2="1">
        <stop offset="0" stop-color="#8a3aa0"/>
        <stop offset="1" stop-color="#4a2a86"/>
      </linearGradient>
    </defs>
    <polygon points="700,0 1200,0 1200,776 430,776" fill="var(--cyan)"/>
    <polygon points="745,0 1200,0 1200,776 470,776" fill="url(#violet)"/>
  </svg>

  <div class="brand">
    <span class="brand-mark"></span>
    <span class="brand-name">NOVALINE</span>
  </div>
  <h1 class="page-title">PRICING</h1>

  <section class="plan-panel"></section>
  <h2 class="plan-title">UNLIMITED SEAT</h2>
  <div class="plan-table"></div>
  <div class="plan-row" style="top:250px"><div class="plan-users">1 User</div><div class="plan-price"><b>$29</b><sup>.99</sup>/month</div></div>
  <div class="plan-row" style="top:296px"><div class="plan-users">2 - 10 Users</div><div class="plan-price"><b>$24</b><sup>.99</sup>/user</div></div>
  <div class="plan-row" style="top:342px"><div class="plan-users">11 - 49 Users</div><div class="plan-price"><b>$21</b><sup>.99</sup>/user</div></div>
  <div class="plan-row" style="top:388px"><div class="plan-users">50 + Users</div><div class="plan-price"><b class="contact">Contact Us!</b></div></div>

  <div class="devices" role="img" aria-label="Desk phone, smartphone, monitor and laptop showing the calling dashboard"></div>

  <div class="addons-panel"></div>
  <div class="addons-tab">ADD ONS</div>

  <div class="addon" style="left:87px;top:518px">
    <div class="addon-icon"><svg viewBox="0 0 24 24"><rect x="9" y="2" width="6" height="12" rx="3"/><path d="M6 11a6 6 0 0 0 12 0h-2a4 4 0 0 1-8 0z"/><rect x="11" y="17" width="2" height="4"/><rect x="8" y="20" width="8" height="2"/></svg></div>
    <div class="addon-name">Call Recording</div><div class="addon-price"><small>Starting at</small>$5/user</div>
  </div>
  <div class="addon" style="left:87px;top:600px">
    <div class="addon-icon"><svg viewBox="0 0 24 24"><rect x="6" y="1" width="12" height="22" rx="2"/><rect x="8" y="4" width="8" height="14" fill="#f2f3f6"/></svg></div>
    <div class="addon-name">Additional Local Numbers</div><div class="addon-price">$1.99/number</div>
  </div>

  <div class="addon" style="left:628px;top:518px">
    <div class="addon-icon"><svg viewBox="0 0 24 24"><rect x="2" y="7" width="5" height="15" rx="1"/><rect x="8" y="2" width="10" height="7"/><rect x="8" y="9" width="14" height="13" rx="1"/><g fill="#f2f3f6"><rect x="11" y="12" width="2" height="2"/><rect x="14" y="12" width="2" height="2"/><rect x="17" y="12" width="2" height="2"/><rect x="11" y="16" width="2" height="2"/><rect x="14" y="16" width="2" height="2"/><rect x="17" y="16" width="2" height="2"/></g></svg></div>
    <div class="addon-name">Fax to Email</div><div class="addon-price"><small>Starting at</small>$8/user</div>
  </div>
  <div class="addon" style="left:628px;top:600px">
    <div class="addon-icon"><svg viewBox="0 0 24 24"><rect x="1" y="1" width="22" height="22" rx="4"/><path fill="#f2f3f6" d="M8 7.5a9 9 0 0 0 4 4l1.3-1.3a.6.6 0 0 1 .6-.15 7 7 0 0 0 2.2.35.6.6 0 0 1 .6.6V13a.6.6 0 0 1-.6.6A10 10 0 0 1 6 5.6.6.6 0 0 1 6.6 5h2a.6.6 0 0 1 .6.6 7 7 0 0 0 .35 2.2.6.6 0 0 1-.15.6z" transform="translate(0 3)"/></svg></div>
    <div class="addon-name">Toll Free Numbers</div><div class="addon-price">$1.99/number<small>plus usage</small></div>
  </div>

  <footer class="footer">
    <span>brightcallnet.com</span><span>|</span><span>855.BRIGHT1</span><span>|</span><span>sales@brightcallnet.com</span>
  </footer>
</div>
</body>
</html>
```